Van Wrap for Stone cleaning and polishing

Create a van wrap that is using our logo and previous wrap designs while incorporating an elegant feel for a natural stone cleaning and polishing division. I would like to include maybe some photographs of marble and granite. Please see our current van wraps for general services. I do want this a lot more elegant since this targets a different customer base. This will go on a 2025 Tarn 3400 Haulwell 159' high roof.

```html
<!DOCTYPE html>
<html lang="en">
<head>
<meta charset="utf-8">
<title>Mesa Vapor Crew – Tarn 3400 Haulwell Wrap</title>
<link rel="stylesheet" href="https://fonts.googleapis.com/css2?family=Montserrat:wght@500;700;800&family=Kaushan+Script&display=swap">
<style>
  :root {
    --navy: #23235e;
    --navy-deep: #1a1a45;
    --cyan: #1ea3d8;
    --cyan-light: #35b8e8;
    --white: #ffffff;
    --paper: #f4f5f7;
    --marble-light: #e6e8ec;
    --marble-mid: #b9bcc4;
    --stone-warm: #a08c72;
    --stone-warm-dark: #6f604e;
    --stone-dark: #4d5560;
    --stone-dark-deep: #2f353d;
  }
  html, body {
    margin: 0;
    width: 1200px;
    height: 2700px;
    overflow: hidden;
    background: var(--white);
  }
  .canvas { position: relative; width: 1200px; height: 2700px; }
  .view { position: absolute; overflow: visible; }
  .view-left  { left: 100px; top: 200px;  width: 1000px; height: 360px; }
  .view-front { left: 360px; top: 800px;  width: 480px;  height: 300px; }
  .view-right { left: 100px; top: 1550px; width: 1000px; height: 360px; }
  .view-rear  { left: 370px; top: 2080px; width: 460px;  height: 480px; }
  .shared-defs { position: absolute; width: 0; height: 0; }

  .brand      { font-family: "Montserrat", sans-serif; font-weight: 700; fill: var(--navy); letter-spacing: 3px; }
  .tagline    { font-family: "Montserrat", sans-serif; font-weight: 700; fill: var(--navy); letter-spacing: 2.5px; }
  .call       { font-family: "Kaushan Script", cursive; fill: var(--cyan-light); }
  .phone      { font-family: "Montserrat", sans-serif; font-weight: 800; fill: var(--cyan-light); }
  .phone-dark { font-family: "Montserrat", sans-serif; font-weight: 800; fill: var(--navy); }
  .service    { font-family: "Montserrat", sans-serif; font-weight: 700; fill: var(--white); font-size: 12px; }
  .web        { font-family: "Montserrat", sans-serif; font-weight: 700; font-style: italic; fill: var(--white); font-size: 12px; letter-spacing: 0.3px; }
  .photo-ring { fill: none; stroke: var(--white); stroke-width: 3; }
</style>
</head>
<body>
<main class="canvas">

  <svg class="shared-defs" aria-hidden="true">
    <defs>
      <symbol id="tick-icon" viewBox="0 0 12 12">
        <circle cx="6" cy="6" r="6" fill="#35b8e8"/>
        <path d="M3.2,6.2 L5.2,8.1 L8.9,4.1" fill="none" stroke="#ffffff" stroke-width="1.6" stroke-linecap="round" stroke-linejoin="round"/>
      </symbol>
      <radialGradient id="photo-marble" cx="35%" cy="30%" r="75%">
        <stop offset="0%" stop-color="#f2f3f6"/>
        <stop offset="100%" stop-color="#a9adb6"/>
      </radialGradient>
      <radialGradient id="photo-warm" cx="35%" cy="30%" r="75%">
        <stop offset="0%" stop-color="#b9a488"/>
        <stop offset="100%" stop-color="#5f5244"/>
      </radialGradient>
      <radialGradient id="photo-dark" cx="35%" cy="30%" r="75%">
        <stop offset="0%" stop-color="#6b7480"/>
        <stop offset="100%" stop-color="#2f353d"/>
      </radialGradient>
    </defs>
  </svg>

  <!-- Driver side panel -->
  <svg class="view view-left" viewBox="0 0 1000 360" aria-label="Driver side wrap panel">
    <defs>
      <clipPath id="body-left"><path d="M0,230 L30,150 L190,30 Q215,10 260,10 L960,10 Q990,10 990,40 L990,340 L0,340 Z"/></clipPath>
    </defs>
    <g clip-path="url(#body-left)">
      <rect width="1000" height="360" fill="var(--white)"/>
      <path d="M620,10 L990,10 L990,340 L300,340 Q560,320 650,200 Q700,100 620,10 Z" fill="var(--navy)"/>
      <path d="M220,300 Q460,300 600,250 L640,340 L220,340 Z" fill="var(--navy-deep)"/>
      <path d="M600,10 Q690,100 640,200 Q560,300 220,305" fill="none" stroke="var(--cyan)" stroke-width="12"/>
      <path d="M560,340 Q660,230 990,200 L990,340 Z" fill="var(--cyan)"/>
      <path d="M540,340 Q650,210 990,185" fill="none" stroke="var(--white)" stroke-width="6"/>
    </g>
    <text class="call" x="676" y="38" font-size="20">Call Today !</text>
    <text class="phone" x="676" y="68" font-size="22">&#9990; 555-014-2286</text>
    <g class="service" transform="translate(696,84)">
      <use href="#tick-icon" x="0" y="0" width="11" height="11"/><text x="16" y="10">CARPET</text>
      <use href="#tick-icon" x="0" y="18" width="11" height="11"/><text x="16" y="28">ORIENTAL RUGS</text>
      <use href="#tick-icon" x="0" y="36" width="11" height="11"/><text x="16" y="46">TILE &amp; GROUT</text>
      <use href="#tick-icon" x="0" y="54" width="11" height="11"/><text x="16" y="64">NATURE STONE</text>
      <use href="#tick-icon" x="0" y="72" width="11" height="11"/><text x="16" y="82">HARDWOOD FLOORS</text>
      <use href="#tick-icon" x="0" y="90" width="11" height="11"/><text x="16" y="100">AIR DUCTS</text>
    </g>
    <text class="web" x="880" y="236" text-anchor="middle">MESAVAPORCREW.COM</text>
    <rect x="350" y="75" width="22" height="22" fill="var(--navy)"/>
    <text class="brand" x="382" y="97" font-size="34">MESA</text>
    <text class="brand" x="350" y="135" font-size="30">VAPOR CREW</text>
    <text class="tagline" x="350" y="162" font-size="13">CLEANING &amp; RESTORATION</text>
    <g class="photo-row">
      <circle cx="250" cy="228" r="33" fill="url(#photo-warm)" role="img" aria-label="Photo of a polished stone floor in a living room"/>
      <circle cx="250" cy="228" r="33" class="photo-ring"/>
      <circle cx="330" cy="218" r="36" fill="url(#photo-marble)" role="img" aria-label="Photo of white marble slab"/>
      <circle cx="330" cy="218" r="36" class="photo-ring"/>
      <circle cx="410" cy="212" r="36" fill="url(#photo-dark)" role="img" aria-label="Photo of a technician cleaning a rug"/>
      <circle cx="410" cy="212" r="36" class="photo-ring"/>
      <circle cx="483" cy="200" r="30" fill="url(#photo-marble)" role="img" aria-label="Photo of a bright marble hallway"/>
      <circle cx="483" cy="200" r="30" class="photo-ring"/>
    </g>
  </svg>

  <!-- Front panel -->
  <svg class="view view-front" viewBox="0 0 480 300" aria-label="Front wrap panel">
    <path d="M20,40 Q240,0 460,40 L440,290 L40,290 Z" fill="var(--paper)"/>
    <rect x="148" y="170" width="12" height="12" fill="var(--navy)"/>
    <text class="brand" x="166" y="182" font-size="16">MESA</text>
    <text class="brand" x="240" y="204" font-size="15" text-anchor="middle">VAPOR CREW</text>
    <text class="tagline" x="240" y="222" font-size="8" text-anchor="middle">CLEANING &amp; RESTORATION</text>
  </svg>

  <!-- Passenger side panel -->
  <svg class="view view-right" viewBox="0 0 1000 360" aria-label="Passenger side wrap panel">
    <defs>
      <clipPath id="body-right"><path d="M0,230 L30,150 L190,30 Q215,10 260,10 L960,10 Q990,10 990,40 L990,340 L0,340 Z"/></clipPath>
    </defs>
    <g transform="translate(1000,0) scale(-1,1)">
      <g clip-path="url(#body-right)">
        <rect width="1000" height="360" fill="var(--white)"/>
        <path d="M620,10 L990,10 L990,340 L300,340 Q560,320 650,200 Q700,100 620,10 Z" fill="var(--navy)"/>
        <path d="M220,300 Q460,300 600,250 L640,340 L220,340 Z" fill="var(--navy-deep)"/>
        <path d="M600,10 Q690,100 640,200 Q560,300 220,305" fill="none" stroke="var(--cyan)" stroke-width="12"/>
        <path d="M560,340 Q660,230 990,200 L990,340 Z" fill="var(--cyan)"/>
        <path d="M540,340 Q650,210 990,185" fill="none" stroke="var(--white)" stroke-width="6"/>
      </g>
    </g>
    <text class="call" x="84" y="38" font-size="20">Call Today !</text>
    <text class="phone" x="84" y="68" font-size="22">&#9990; 555-014-2286</text>
    <g class="service" transform="translate(104,84)">
      <use href="#tick-icon" x="0" y="0" width="11" height="11"/><text x="16" y="10">CARPET</text>
      <use href="#tick-icon" x="0" y="18" width="11" height="11"/><text x="16" y="28">ORIENTAL RUGS</text>
      <use href="#tick-icon" x="0" y="36" width="11" height="11"/><text x="16" y="46">TILE &amp; GROUT</text>
      <use href="#tick-icon" x="0" y="54" width="11" height="11"/><text x="16" y="64">NATURE STONE</text>
      <use href="#tick-icon" x="0" y="72" width="11" height="11"/><text x="16" y="82">HARDWOOD FLOORS</text>
      <use href="#tick-icon" x="0" y="90" width="11" height="11"/><text x="16" y="100">AIR DUCTS</text>
    </g>
    <text class="web" x="120" y="236" text-anchor="middle">MESAVAPORCREW.COM</text>
    <rect x="420" y="75" width="22" height="22" fill="var(--navy)"/>
    <text class="brand" x="452" y="97" font-size="34">MESA</text>
    <text class="brand" x="420" y="135" font-size="30">VAPOR CREW</text>
    <text class="tagline" x="420" y="162" font-size="13">CLEANING &amp; RESTORATION</text>
    <g class="photo-row">
      <circle cx="517" cy="200" r="30" fill="url(#photo-marble)" role="img" aria-label="Photo of a bright marble hallway"/>
      <circle cx="517" cy="200" r="30" class="photo-ring"/>
      <circle cx="590" cy="212" r="36" fill="url(#photo-dark)" role="img" aria-label="Photo of a technician cleaning a rug"/>
      <circle cx="590" cy="212" r="36" class="photo-ring"/>
      <circle cx="670" cy="218" r="36" fill="url(#photo-marble)" role="img" aria-label="Photo of white marble slab"/>
      <circle cx="670" cy="218" r="36" class="photo-ring"/>
      <circle cx="750" cy="228" r="33" fill="url(#photo-warm)" role="img" aria-label="Photo of a polished stone floor in a living room"/>
      <circle cx="750" cy="228" r="33" class="photo-ring"/>
    </g>
  </svg>

  <!-- Rear doors -->
  <svg class="view view-rear" viewBox="0 0 460 480" aria-label="Rear door wrap panel">
    <defs>
      <clipPath id="body-rear"><rect x="0" y="0" width="460" height="480" rx="14"/></clipPath>
    </defs>
    <g clip-path="url(#body-rear)">
      <rect width="460" height="480" fill="var(--white)"/>
      <path d="M300,0 L460,0 L460,480 L0,480 L0,360 Q330,330 390,200 Q420,90 300,0 Z" fill="var(--navy)"/>
      <path d="M280,0 Q400,90 370,200 Q320,320 0,340" fill="none" stroke="var(--cyan)" stroke-width="12"/>
      <path d="M150,480 Q250,380 460,350 L460,480 Z" fill="var(--cyan)"/>
      <path d="M130,480 Q240,365 460,335" fill="none" stroke="var(--white)" stroke-width="6"/>
      <line x1="230" y1="0" x2="230" y2="480" stroke="#c8cbd2" stroke-width="1.5"/>
    </g>
    <text class="call" x="110" y="48" font-size="20">Call Today !</text>
    <text class="phone-dark" x="110" y="78" font-size="22">&#9990; 555-014-2286</text>
    <rect x="110" y="140" width="20" height="20" fill="var(--navy)"/>
    <text class="brand" x="140" y="160" font-size="30">MESA</text>
    <text class="brand" x="110" y="196" font-size="26">VAPOR CREW</text>
    <text class="tagline" x="110" y="222" font-size="12">CLEANING &amp; RESTORATION</text>
    <g class="photo-row">
      <circle cx="65" cy="295" r="23" fill="url(#photo-warm)" role="img" aria-label="Photo of a polished stone floor"/>
      <circle cx="65" cy="295" r="23" class="photo-ring"/>
      <circle cx="120" cy="290" r="24" fill="url(#photo-marble)" role="img" aria-label="Photo of white marble slab"/>
      <circle cx="120" cy="290" r="24" class="photo-ring"/>
      <circle cx="175" cy="285" r="24" fill="url(#photo-dark)" role="img" aria-label="Photo of a technician cleaning a rug"/>
      <circle cx="175" cy="285" r="24" class="photo-ring"/>
      <circle cx="225" cy="280" r="20" fill="url(#photo-marble)" role="img" aria-label="Photo of a marble hallway"/>
      <circle cx="225" cy="280" r="20" class="photo-ring"/>
    </g>
    <text class="web" x="335" y="432" text-anchor="middle">MESAVAPORCREW.COM</text>
  </svg>

</main>
</body>
</html>
```